Create a Modern, On-Brand Zoom Background for Our LUMORA Webinar Team

Project Overview
We are hosting a Zoom webinar next month and want all team members to appear unified on-screen. We need a custom, branded Zoom background that incorporates our corporate identity while remaining clean, modern, and visually polished.
Design Requirements
File Type: Static image (no motion) optimized for Zoom virtual backgrounds
Orientation: 16:9 landscape
Main Logo: KALDRIN (primary)
Secondary Logo: LUMORA (supporting logo)
Design Style:
Clean, crisp, modern
Professional and easy on the eyes
Eye-catching but not busy or distracting
Bold enough to look strong on-camera but minimal enough to sit behind presenters
Color Palette: Use Kaldrin brand colors, LUMORA colors, or a subtle combination
Avoid: Clutter, heavy textures, distracting patterns, excessive gradients, motion effects
Preferred (Not Required)
Designs created in Canva are strongly preferred.
Designers who provide:
Editable Canva link
…will be prioritized, as this allows us to make future updates easily.
Deliverables
Final Zoom-ready JPG/PNG background
Source files (Canva preferred; AI/PSD acceptable)
Audience & Use Case
This background will be used by internal Kaldrin team members during a high-visibility webinar with physicians and clinical partners involved in the LUMORA study.

```html
<!DOCTYPE html>
<html lang="en">
<head>
<meta charset="utf-8">
<title>Kaldrin Webinar Backgrounds</title>
<link rel="stylesheet" href="https://fonts.googleapis.com/css2?family=Oswald:wght@300;500&display=swap">
<style>
  :root {
    --page: #ffffff;
    --navy-deep: #060e3a;
    --navy: #0b1a63;
    --band: #2a4fc4;
    --band-glow: #3d66e0;
    --lime: #5fd615;
    --forest: #1f5a2a;
    --star: #7fb8ff;
    --ink-light: #ffffff;
    --photo-coat: #d9dde3;
    --photo-shirt: #3d5580;
  }
  html, body {
    margin: 0;
    width: 1008px;
    height: 1200px;
    overflow: hidden;
    background: var(--page);
  }
  .sheet {
    position: relative;
    width: 1008px;
    height: 1200px;
  }
  .backdrop {
    position: absolute;
    left: 63px;
    width: 881px;
    height: 496px;
    overflow: hidden;
    background: var(--navy);
  }
  .backdrop--presenter { top: 75px; }
  .backdrop--empty { top: 635px; }
  .backdrop__art {
    position: absolute;
    inset: 0;
    width: 100%;
    height: 100%;
  }
  .brand-primary {
    position: absolute;
    left: 47px;
    top: 40px;
    margin: 0;
    font-family: "Oswald", sans-serif;
    font-weight: 300;
    font-size: 72px;
    line-height: 1;
    letter-spacing: 2px;
    color: var(--ink-light);
  }
  .brand-study {
    position: absolute;
    left: 46px;
    top: 422px;
    font-family: "Oswald", sans-serif;
    font-weight: 500;
    color: var(--ink-light);
  }
  .brand-study__name {
    display: block;
    font-size: 28px;
    line-height: 1;
    letter-spacing: 0.5px;
  }
  .brand-study__tagline {
    display: block;
    margin-top: 2px;
    font-size: 4.4px;
    letter-spacing: 0.1px;
    white-space: nowrap;
  }
  .presenter-photo {
    position: absolute;
    left: 247px;
    top: 65px;
    width: 395px;
    height: 431px;
    border-radius: 160px 160px 0 0;
    background: linear-gradient(180deg, rgba(140,140,140,0.35) 0%, var(--photo-shirt) 45%, var(--photo-coat) 60%, var(--photo-coat) 100%);
  }
</style>
</head>
<body>
<main class="sheet">

  <section class="backdrop backdrop--presenter">
    <svg class="backdrop__art" viewBox="0 0 881 496" preserveAspectRatio="none" aria-hidden="true">
      <defs>
        <radialGradient id="limeGlowA" cx="0" cy="0" r="1" gradientUnits="userSpaceOnUse" gradientTransform="translate(0 0) scale(560 420)">
          <stop offset="0" stop-color="#5fd615"/>
          <stop offset="0.35" stop-color="#1f5a2a"/>
          <stop offset="0.75" stop-color="#0b1a63" stop-opacity="0"/>
        </radialGradient>
      </defs>
      <rect width="881" height="496" fill="#0b1a63"/>
      <polygon points="468,0 881,0 881,62 695,248" fill="#060e3a" opacity="0.85"/>
      <polygon points="640,496 695,300 881,470 881,496" fill="#08134a" opacity="0.6"/>
      <line x1="440" y1="-30" x2="900" y2="470" stroke="#2a4fc4" stroke-width="50" stroke-opacity="0.45"/>
      <line x1="905" y1="38" x2="440" y2="505" stroke="#2a4fc4" stroke-width="50" stroke-opacity="0.55"/>
      <line x1="905" y1="55" x2="660" y2="300" stroke="#3d66e0" stroke-width="6" stroke-opacity="0.8"/>
      <rect width="881" height="496" fill="url(#limeGlowA)"/>
      <g fill="#7fb8ff">
        <circle cx="380" cy="30" r="1.2"/><circle cx="425" cy="49" r="1"/><circle cx="570" cy="205" r="1.5"/>
        <circle cx="85" cy="328" r="1.2"/><circle cx="85" cy="370" r="1"/><circle cx="250" cy="405" r="1"/>
        <circle cx="49" cy="484" r="1"/><circle cx="410" cy="90" r="1"/>
      </g>
      <g fill="#8ee05a" opacity="0.7">
        <circle cx="50" cy="147" r="1.5"/><circle cx="118" cy="35" r="1.2"/><circle cx="175" cy="180" r="1"/>
        <circle cx="230" cy="215" r="1"/><circle cx="305" cy="55" r="1"/>
      </g>
    </svg>
    <h1 class="brand-primary">KALDRIN</h1>
    <div class="presenter-photo" role="img" aria-label="Portrait photo of a clinician in a white lab coat, arms crossed"></div>
    <div class="brand-study">
      <span class="brand-study__name">LUMORA U.S.</span>
      <span class="brand-study__tagline">NOVA Disc Randomized, Sham-Controlled, Multi-Center, Double Blind Clinical Trial</span>
    </div>
  </section>

  <section class="backdrop backdrop--empty">
    <svg class="backdrop__art" viewBox="0 0 881 496" preserveAspectRatio="none" aria-hidden="true">
      <defs>
        <radialGradient id="limeGlowB" cx="0" cy="0" r="1" gradientUnits="userSpaceOnUse" gradientTransform="translate(0 0) scale(560 420)">
          <stop offset="0" stop-color="#5fd615"/>
          <stop offset="0.35" stop-color="#1f5a2a"/>
          <stop offset="0.75" stop-color="#0b1a63" stop-opacity="0"/>
        </radialGradient>
      </defs>
      <rect width="881" height="496" fill="#0b1a63"/>
      <polygon points="468,0 881,0 881,62 695,248" fill="#060e3a" opacity="0.85"/>
      <polygon points="640,496 695,300 881,470 881,496" fill="#08134a" opacity="0.6"/>
      <line x1="440" y1="-30" x2="900" y2="470" stroke="#2a4fc4" stroke-width="50" stroke-opacity="0.45"/>
      <line x1="905" y1="38" x2="440" y2="505" stroke="#2a4fc4" stroke-width="50" stroke-opacity="0.55"/>
      <line x1="905" y1="55" x2="660" y2="300" stroke="#3d66e0" stroke-width="6" stroke-opacity="0.8"/>
      <rect width="881" height="496" fill="url(#limeGlowB)"/>
      <g fill="#7fb8ff">
        <circle cx="380" cy="30" r="1.2"/><circle cx="425" cy="49" r="1"/><circle cx="570" cy="205" r="1.5"/>
        <circle cx="85" cy="328" r="1.2"/><circle cx="85" cy="370" r="1"/><circle cx="250" cy="405" r="1"/>
        <circle cx="49" cy="484" r="1"/><circle cx="410" cy="90" r="1"/>
      </g>
      <g fill="#8ee05a" opacity="0.7">
        <circle cx="50" cy="147" r="1.5"/><circle cx="118" cy="35" r="1.2"/><circle cx="175" cy="180" r="1"/>
        <circle cx="230" cy="215" r="1"/><circle cx="305" cy="55" r="1"/>
      </g>
    </svg>
    <h2 class="brand-primary">KALDRIN</h2>
    <div class="brand-study">
      <span class="brand-study__name">LUMORA U.S.</span>
      <span class="brand-study__tagline">NOVA Disc Randomized, Sham-Controlled, Multi-Center, Double Blind Clinical Trial</span>
    </div>
  </section>

</main>
</body>
</html>
```